Flyer & Business Card for Lakeside Lens Circle photography courses

I need a flyer design for my company Lakeside Lens Circle - which offers photography classes for all levels in Geneva / Switzerland.

The flyer has to have an attractive visual at the front, and should highlight different types of classes and our teaching philosophy in the back.

Especially the images of Geneva (you can find some on lakesidelenscircle.example and also on my photography website www.morvekimages.example) will help to make people appreciate it's local.

Please check my website to learn more about my company, the logo, brand identity and the overall feeling:
https://www.lakesidelenscircle.example

For the colors, I have used blue in the website and the logo, so it should be somehow compatible.

The final design should communicate fun courses offered by professional photographers that have received consistently 5 star ratings.

Target Market(s)

Geneva / Switzerland

Industry/Entity Type

Business

Contact Information for Business Card

Double sided - front could be a photo (or multiple photos that could be printed as part of one order from pribo.example) and the back should communicate the brand identity.

Colors
0292cd
33a6d7
0555a3

```html
<!DOCTYPE html>
<html lang="en">
<head>
<meta charset="utf-8">
<title>Lakeside Lens Circle – Flyer</title>
<link href="https://fonts.googleapis.com/css2?family=Fira+Sans:ital,wght@0,400;0,600;0,700;1,700&family=Roboto:wght@400;500;700&display=swap" rel="stylesheet">
<style>
:root{
  --bg:#e9e4d8;
  --ink:#111418;
  --white:#ffffff;
  --brand:#0292cd;
  --brand-light:#33a6d7;
  --brand-deep:#0555a3;
  --royal:#1f5fe0;
  --band:#2a8ad6;
  --muted:#c9d6e6;
  --accent-teal:#2fb6c9;
  --gold:#5a3d14;
}
*{margin:0;padding:0;box-sizing:border-box}
html,body{width:1200px;height:838px;overflow:hidden;background:var(--bg)}
body{position:relative;font-family:"Roboto",Arial,sans-serif;color:var(--white)}
.page{position:absolute;top:30px;width:515px;height:753px;overflow:hidden;box-shadow:0 10px 28px rgba(0,0,0,.35)}
.page--front{left:70px;background:linear-gradient(180deg,#161a20 0%,#2b2e34 60%,#3a3d42 100%)}
.page--back{left:614px;background:#0a0f18}
.abs{position:absolute}

/* front */
.hero-photo{left:0;top:0;width:515px;height:345px;background:radial-gradient(circle at 36% 62%,#1b1b1d 0 24%,#3a3636 38%,transparent 56%),radial-gradient(circle at 20% 40%,#6a4a40 0,transparent 40%),linear-gradient(135deg,#2a2a2c,#5b5a58 55%,#2c2b2b)}
.logo{left:303px;top:21px;width:194px;height:82px;background:var(--white);display:flex;align-items:center;gap:10px;padding:0 12px}
.logo__dot{width:44px;height:44px;border-radius:50%;background:var(--ink);flex:none}
.logo__name{font-family:"Fira Sans",sans-serif;font-weight:600;font-size:19px;line-height:1.05;color:var(--ink)}
.hero-title{right:18px;top:118px;text-align:right;font-family:"Roboto",sans-serif;font-weight:500;font-size:24px;line-height:30px;letter-spacing:.3px}
.strip{left:0;top:354px;width:515px;height:129px}
.intro{left:12px;top:502px;width:420px;font-size:14px;line-height:18px}
.intro b{color:var(--brand-light)}
.cta{left:0;top:555px;width:470px;height:41px;background:linear-gradient(90deg,var(--brand-deep),#2f7fc8 80%,rgba(47,127,200,.2));padding:4px 0 0 17px}
.cta__title{font-size:18px;font-weight:500;line-height:21px}
.cta__sub{font-size:9.5px;padding-left:20px}
.bridge{left:0;top:490px;width:515px;height:263px}
.front-contact{left:0;top:707px;width:380px;height:46px;background:linear-gradient(90deg,#2f6fb0,rgba(47,111,176,.4));padding:4px 12px;font-weight:700;font-size:10.5px;line-height:12.5px}
.front-contact .url{font-size:13px}

/* back */
.topbar{left:0;top:0;width:515px;height:21px;background:linear-gradient(180deg,var(--royal),var(--brand-deep))}
.headline{left:0;top:21px;width:515px;height:50px;background:#05080d;font-family:"Fira Sans",sans-serif;font-style:italic;font-weight:700;font-size:25px;line-height:50px;padding-left:28px}
.city-photo{left:0;top:75px;width:515px;height:255px}
.courses-bar{left:0;top:283px;width:515px;height:47px;background:linear-gradient(180deg,rgba(20,60,140,0),rgba(25,85,190,.9));font-family:"Fira Sans",sans-serif;font-style:italic;font-weight:700;font-size:23px;padding:15px 0 0 24px}
.courses-bar span{color:var(--gold)}
.cols{left:0;top:335px;width:515px;height:172px;display:flex;gap:4px}
.col{flex:1;background:linear-gradient(180deg,#0e2a52,#123d73);padding:9px 8px;position:relative}
.col h3{font-family:"Fira Sans",sans-serif;font-weight:600;font-size:11px;line-height:13px;margin-bottom:9px}
.col p{font-size:6.3px;line-height:8.3px;text-align:justify}
.col .rec{font-weight:700;font-size:7.5px;text-align:center;margin-bottom:6px}
.col .center{text-align:center}
.col ul{list-style:none;font-size:6.6px;line-height:12px;color:var(--muted)}
.col li::before{content:"› ";color:var(--brand-light)}
.pill{position:absolute;left:10px;right:10px;bottom:8px;height:37px;border-radius:18px;background:linear-gradient(180deg,var(--accent-teal),#1776b8);text-align:center;padding-top:5px}
.pill b{font-size:9px;display:block}
.pill small{font-size:6.3px;line-height:7.5px;display:block}
.pill--short{height:22px;padding-top:7px}
.reviews{left:0;top:510px;width:515px;height:164px;background:linear-gradient(180deg,var(--band),#2d84d2)}
.reviews h2{position:absolute;left:10px;top:7px;font-weight:500;font-size:24px;letter-spacing:-.2px}
.review{position:absolute;background:var(--white);color:#333;border:1px solid #dde;font-size:6.2px;line-height:8.5px;padding:6px 7px}
.review__head{display:flex;gap:5px;align-items:center;margin-bottom:6px;color:#666}
.review__head b{color:var(--brand-deep)}
.avatar{width:14px;height:14px;background:#b9a89a;flex:none}
.review__foot{position:absolute;left:7px;bottom:5px;right:7px;border-top:1px solid #e3e3e3;padding-top:3px;color:#777;word-spacing:18px}
.back-footer{left:0;top:674px;width:515px;height:79px;background:linear-gradient(90deg,#020305,#0d2c5a 50%,#2c82d0);text-align:center;padding-top:9px}
.back-footer h4{font-weight:500;font-size:18px;margin-bottom:3px}
.back-footer p{font-weight:700;font-size:9.3px;line-height:10.5px}
</style>
</head>
<body>

<section class="page page--front">
  <div class="abs hero-photo" role="img" aria-label="Close-up of a photographer holding a camera lens toward the viewer"></div>
  <div class="abs logo"><span class="logo__dot"></span><span class="logo__name">Lakeside Lens Circle</span></div>
  <h1 class="abs hero-title">PROFESSIONAL PHOTOGRAPHY<br>STUDIO</h1>

  <svg class="abs strip" viewBox="0 0 515 129" aria-hidden="true">
    <defs>
      <linearGradient id="gGrey" x1="0" y1="0" x2="0" y2="1"><stop offset="0" stop-color="#3a3a3a"/><stop offset=".6" stop-color="#bdbdbd"/><stop offset="1" stop-color="#222"/></linearGradient>
      <linearGradient id="gDusk" x1="0" y1="0" x2="0" y2="1"><stop offset="0" stop-color="#2c2f36"/><stop offset=".5" stop-color="#7c7d76"/><stop offset="1" stop-color="#3b4a2a"/></linearGradient>
      <linearGradient id="gLake" x1="0" y1="0" x2="0" y2="1"><stop offset="0" stop-color="#2f62c8"/><stop offset=".5" stop-color="#d9b66a"/><stop offset="1" stop-color="#1a4d9a"/></linearGradient>
    </defs>
    <rect width="515" height="129" fill="#0b0d10"/>
    <polygon points="0,0 140,0 215,129 0,129" fill="url(#gGrey)" role="img" aria-label="Black and white lakeside building"/>
    <polygon points="147,0 285,0 325,129 222,129" fill="url(#gDusk)" role="img" aria-label="Country path under a cloudy evening sky"/>
    <polygon points="292,0 515,0 515,129 332,129" fill="url(#gLake)" role="img" aria-label="Lake harbour at dusk with city lights"/>
  </svg>

  <svg class="abs bridge" viewBox="0 0 515 263" aria-hidden="true">
    <defs><linearGradient id="gBridge" x1="0" y1="0" x2="1" y2="1"><stop offset="0" stop-color="#1a1e8a"/><stop offset=".45" stop-color="#d04a7a"/><stop offset=".7" stop-color="#1c5fcf"/><stop offset="1" stop-color="#17a0e6"/></linearGradient></defs>
    <polygon points="393,30 515,30 515,263 294,263" fill="url(#gBridge)" role="img" aria-label="Illuminated footbridge at night"/>
  </svg>

  <p class="abs intro">Photography courses and workshops to suit all levels of skill and experience, in central <b>Geneva /Switzerland.</b></p>
  <div class="abs cta">
    <div class="cta__title">Start taking better pictures immediately</div>
    <div class="cta__sub">We don’t lose time on theory, we just show you how to do it</div>
  </div>
  <div class="abs front-contact">
    CONTACT US NOW : +41 70 555 01 23<br>
    VISIT OUR WEBSITE FOR MORE INFORMATION<br>
    <span class="url">www.lakesidelenscircle.example</span>
  </div>
</section>

<section class="page page--back">
  <div class="abs topbar"></div>
  <h2 class="abs headline">Ready to kick-start your photography?</h2>
  <div class="abs city-photo" role="img" aria-label="Geneva lakefront at blue hour with the water jet and lit hotels" style="background:linear-gradient(180deg,#3f6fe6 0%,#2c58d8 35%,#b9a77a 52%,#2c4fb8 70%,#1a3f9a 100%)"></div>
  <div class="abs courses-bar">DIGITAL PHOTOGRAPHY <span>Courses for all levels</span></div>

  <div class="abs cols">
    <article class="col">
      <h3>Intensive photography courses for beginers</h3>
      <p>A 7 hours DSLR photography course aimed at total beginners with extended hands-on activities. The first 4 hours, we will give you all the practical knowledge you need with concrete examples. In the second part, we will practice together all the concepts that we have learned and review your work.</p>
      <div class="pill"><b>Choose this class if</b><small>You want to see a significant improvement<br>on your photography immediately.</small></div>
    </article>
    <article class="col">
      <h3>Weekend photography classes for beginers</h3>
      <p class="rec">Our ultimate recommendation:</p>
      <p class="center">A total 10 hours photography course that takes place over 5 weeks after work, aimed at busy professionals. Every week we meet for two hours to go through key concepts, then give interesting and challenging assignments to review the results next week.</p>
      <div class="pill"><b>Choose this class if</b><small>You love photography and would love to focus on it during five weeks to make a serious improvement.</small></div>
    </article>
    <article class="col">
      <h3>Other photography courses for all level</h3>
      <ul>
        <li>Half-day Course for Beginners</li>
        <li>Intermediate Photography Course</li>
        <li>Street Photography Course</li>
        <li>Portrait &amp; Studio Lighting Course</li>
        <li>Lightroom for Photographers Course</li>
        <li>Photoshop for Photographers Course</li>
        <li>Night and Low Light Photography Course</li>
        <li>One to One Private Courses</li>
      </ul>
      <div class="pill pill--short"><b>Photography Gift Vouchers</b></div>
    </article>
  </div>

  <section class="abs reviews">
    <h2>WE GOT GREAT REVIEWS BY OUR CUSTOMER</h2>
    <div class="review" style="left:9px;top:43px;width:252px;height:88px">
      <div class="review__head"><span class="avatar"></span><span><b>Clara Benoit</b> reviewed Lakeside Lens Circle<br>November 22 at 10:12pm</span></div>
      An excellent way to bond with your camera and to learn all its little quirks and how to convert them to your benefit. A day well spent with much useful information gained. Thank you !!
      <div class="review__foot">Like Comment Share</div>
    </div>
    <div class="review" style="left:302px;top:45px;width:199px;height:87px">
      <div class="review__head"><span class="avatar"></span><span><b>Ines Morand</b> reviewed Lakeside Lens Circle<br>July 24</span></div>
      excellent training. Friendly teacher, all the basics you need to know to master your camera. I loved it. Highly recommended !
      <div class="review__foot">Like Comment Share</div>
    </div>
  </section>

  <footer class="abs back-footer">
    <h4>For further information please contact us</h4>
    <p>CONTACT US NOW : +41 70 555 01 23<br>OR<br>VISIT OUR WEBSITE FOR MORE INFORMATION<br>www.lakesidelenscircle.example</p>
  </footer>
</section>

</body>
</html>
```